Kunststoffverpackung für Falkor Snacks
Zielgruppe
Wir sind ein kleines Unternehmen, welches Bisonfleisch aus Nordamerika importiert und vertreibt. Unser neustes Produkt sind Falkor Snacks, deren Verpackung wir uns gerne designen lassen möchten.
Aufgabenstellung:
Design Entwurf für eine Kunststoffverpackung für Falkor Snacks (Trockenfleisch), von kanadischem Bison.
Preissegment: hochpreisig
Verkauf: Delikatessengeschäfte, hochpreisige Kaufhäuser (zb Lumhaus Berlin)
Design: edel, understatement, wenige ausgewählte Farben
Implizierte Message: hochwertiges, nachhaltiges Produkt für Feinschmecker und gesundheitsbewusste Sportler/Abenteurer.
USP: Jerky aus original kanadischem Bisonfleisch, artgerecht aufgezogen, ohne Medikamente, Wachstumshormone oder Futterzusätze
Besondere Produkteigenschaft: Kein Zucker, hoher Proteinanteil, hoher Eisenanteil, niedriger Cholesterinwert, kaum Fett, wenig Salz.
Aufgabenstellung
Zusätzliche Infos zu unserem Bisonfleisch findest du hier:
https://weidekorn-example.de/blogs/news/uber-uns-bisonfleisch-das-beste-fleisch-der-welt
https://weidekorn-example.de/blogs/news/bison-steak-guide
Zusätzliche Informationen zu Bisons findest du hier:
https://weidekorn-example.de/pages/bison-wiki
Auf der Rückseite bitte Platz lassen für folgende Grafiken/Informationen, daher bitte Platzhalter einfügen:
- Zutatenliste
- Nährwerttabelle
- Strichcode
- Recyclinglabel
Maße für die Verpackung sind:
170mm Länge
130mm Breite
Fotos wie die Verpackung auf keinen Fall aussehen sollen befinden sich mit dem Namen 'Dont' anbei. Verpackungen die uns vom Design gefallen befinden sich mit dem Namen 'Do' anbei.
Bei Rückfragen bitte mobil oder per mail wenden an:
Matthias Oldörp

```html
<!DOCTYPE html>
<html lang="de">
<head>
<meta charset="utf-8">
<title>Falkor Snacks – Verpackung Vorderseite</title>
<link rel="stylesheet" href="https://fonts.googleapis.com/css2?family=Alfa+Slab+One&family=Roboto:wght@300&display=swap">
<style>
  :root {
    --backdrop: #d9d9d7;
    --pack: #cfc6ae;
    --pill: #c6bda6;
    --icon-disc: #c4bba3;
    --icon-line: #ddd7c8;
    --brand: #77735f;
    --title: #e5e2dc;
    --ink: #1d1b17;
    --label: #868170;
    --claim: #faf8f3;
    --meat-a: #e0605a;
    --meat-b: #a8404a;
    --meat-c: #7a3a44;
  }
  * { margin: 0; padding: 0; box-sizing: border-box; }
  html, body { width: 1156px; height: 1200px; overflow: hidden; background: var(--backdrop); }
  .package {
    position: absolute; left: 187px; top: 37px; width: 778px; height: 1016px;
    background: var(--pack); overflow: hidden;
    font-family: "Alfa Slab One", serif;
  }
  .brand-mark {
    position: absolute; left: 153px; top: 100px; width: 472px;
    display: flex; align-items: center; justify-content: center; gap: 16px;
    color: var(--brand); font-size: 46px; line-height: 1;
  }
  .brand-mark .dot { width: 26px; height: 26px; border-radius: 50%; background: var(--brand); }
  .product-photo {
    position: absolute; left: 246px; top: 237px; width: 280px; height: 465px; z-index: 1;
    border-radius: 46% 40% 42% 48% / 30% 28% 34% 32%;
    background: radial-gradient(ellipse at 40% 40%, var(--meat-a), var(--meat-b) 60%, var(--meat-c));
    opacity: 0.85;
  }
  .pill {
    position: absolute; z-index: 2; background: var(--pill); color: var(--claim);
    font-size: 18.5px; line-height: 24px; letter-spacing: 0.3px; white-space: nowrap;
    display: flex; align-items: center; justify-content: flex-end; text-align: right;
  }
  .pill--left { left: 0; border-radius: 0 40px 40px 0; }
  .pill--right { right: 0; border-radius: 40px 0 0 40px; padding-right: 16px; }
  .pill--1 { top: 547px; height: 64px; }
  .pill--2 { top: 627px; height: 38px; }
  .pill--left.pill--1 { width: 290px; padding-right: 40px; }
  .pill--left.pill--2 { width: 278px; padding-right: 25px; }
  .pill--right.pill--1 { width: 282px; }
  .pill--right.pill--2 { width: 270px; }
  .title {
    position: absolute; left: 0; width: 778px; top: 752px; text-align: center;
    color: var(--title); font-size: 88px; line-height: 1; letter-spacing: 1px;
  }
  .subtitle {
    position: absolute; left: 54px; top: 845px; color: var(--ink);
    font-size: 28px; line-height: 1; letter-spacing: 0.3px;
  }
  .benefits { position: absolute; left: 0; top: 911px; width: 778px; height: 100px; }
  .benefit { position: absolute; width: 140px; margin-left: -70px; text-align: center; }
  .benefit svg { display: block; margin: 0 auto; }
  .benefit span {
    display: block; margin-top: 11px; font-family: "Roboto", sans-serif; font-weight: 300;
    font-size: 12.5px; letter-spacing: -0.3px; color: var(--label);
  }
  .disc { fill: var(--icon-disc); }
  .glyph { fill: none; stroke: var(--icon-line); stroke-width: 1.6; stroke-linecap: round; stroke-linejoin: round; }
</style>
</head>
<body>
<main class="package">
  <div class="brand-mark"><span class="dot"></span><span>Falkor Snacks</span></div>

  <div class="product-photo" role="img" aria-label="Fallende Scheiben getrockneten Bison-Jerkys"></div>

  <div class="pill pill--left pill--1">hochwertiges,<br>nachhaltiges Produkt</div>
  <div class="pill pill--left pill--2">artgerecht aufgezogen</div>
  <div class="pill pill--right pill--1">ohne Medikamente &amp;<br>Wachstumshormone</div>
  <div class="pill pill--right pill--2">ohne&nbsp; Futterzusätze</div>

  <h1 class="title">Falkor Snacks</h1>
  <p class="subtitle">aus original kanadischem Bisonfleisch</p>

  <section class="benefits">
    <div class="benefit" style="left:146px">
      <svg width="70" height="70" viewBox="0 0 70 70"><circle class="disc" cx="35" cy="35" r="35"/>
        <path class="glyph" d="M26 34l8-4 8 4v9l-8 4-8-4zM34 38v9M26 34l8 4 8-4M36 26l6-3 6 3v7"/><path class="glyph" d="M14 50L54 22"/></svg>
      <span>kein Zucker</span>
    </div>
    <div class="benefit" style="left:273px">
      <svg width="70" height="70" viewBox="0 0 70 70"><circle class="disc" cx="35" cy="35" r="35"/>
        <path class="glyph" d="M14 44c8 4 10-16 18-12s8 8 14-2 8-6 12-4M14 38c6 8 12-8 18-6s10 10 16 0 6-6 10-8"/></svg>
      <span>hoher Proteinanteil</span>
    </div>
    <div class="benefit" style="left:391px">
      <svg width="70" height="70" viewBox="0 0 70 70"><circle class="disc" cx="35" cy="35" r="35"/>
        <path class="glyph" d="M35 16c-6 10-11 16-11 23a11 11 0 0 0 22 0c0-7-5-13-11-23zM30 42a5 5 0 0 0 5 5"/><path class="glyph" d="M14 50L56 22"/></svg>
      <span>kaum Fett</span>
    </div>
    <div class="benefit" style="left:512px">
      <svg width="70" height="70" viewBox="0 0 70 70"><circle class="disc" cx="35" cy="35" r="35"/>
        <path class="glyph" d="M33 16c-6 10-11 16-11 23a11 11 0 0 0 16 10"/><path class="glyph" d="M33 16c4 7 8 12 10 17M43 36v14M38 45l5 5 5-5"/></svg>
      <span>niedriges Cholesterin</span>
    </div>
    <div class="benefit" style="left:624px">
      <svg width="70" height="70" viewBox="0 0 70 70"><circle class="disc" cx="35" cy="35" r="35"/>
        <path class="glyph" d="M30 24a5 5 0 0 1 10 0v4l3 4v16H27V32l3-4z"/><path class="glyph" d="M14 50L56 22"/></svg>
      <span>wenig Salz</span>
    </div>
  </section>
</main>
</body>
</html>
```